Clean & Inspiring Web Design Project

Larkspur Prototype Studio, LLC (also known as LP-Studio) is a company which provides 3D printing services and products. The emphasis is on making these products and services available to the mass-market - customers and users who may or may not have prior experience with 3D printing and/or rapid prototyping technologies. We are a start-up company, looking to build a clean and creativity inspiring brand - our site must encourage visitor to engage and make something. Our aim is to help take mere ideas and turn them into tangible items. We want to show a fusion of ideas (e.g. pencil sketches on graph paper) with design tools (e.g. CAD and drafting software) and rapid prototyping (e.g. TinkNod 3D printers, Stereolithography Machines, etc.). We would like the website to appear professional but at the same time easy to navigate and a good balance between text and pictures. The final design should inspire customers to nurture their ideas into real products and communicate our services to our customers. Our site should have the feel of a vibrant social community with the added benefit of tangible physical creations.

Target Market(s)

People with great ideas that need to be designed into a real product

Industry/Entity Type

Printing

Requirements
Must have
• - Website design should include 2 layouts - one for a "landing page" and one for a "content page"
- Website design must incorporate attached company logo (or derivative of this logo)
- Website design should incorporate the menu options shown in the attached PDF UI concept (UI does not necessarily need to look like the provided concept, just include all the clickable elements)
- Website design must portray an innovative and cooperative design environment with a look-and-feel that appeals to both amateur and professional designers.
- Please include pictures, illustrations and photographs (as needed) related to 3D printing, CAD design, conventional drafting, engineering and manufacturing industries.
- Design should support scaling to multiple screen sizes, from tablet computers (e.g. Slabix) to very large screen PCs.
- Design should include Username & Password fields for login or a button to pull up a login popup.
Nice to have
• - Website design could include "Invent", "Make", "Produce" and "Buy" options that slowly cycle through - with appropriate photos / graphics. These "menu options" would also be mouse-over enabled to switch into the appropriate context as the cursor enters that region (e.g. mouse over the "Invent" text would bring up page 2, etc.). (See attached Original UI Thoughts)
Should not have
• Requirements - Should Not Have:
- Website design should not portray a service that is very expensive or complicated - we are a reasonably priced service meant to be friendly with amateur inventors
- Website design should not be overly complicated - please keep it reasonably simple
- Website design should not be overly trendy
- Website design should not use more than 2 font styles, gaudy fonts, etc.
- Website design should not be "campy" or "tacky" - playful is ok, but please keep it elegant
- Website design should not be overly masculine or feminine - we will have both women and men as customers

```html
<!DOCTYPE html>
<html lang="en">
<head>
<meta charset="utf-8">
<title>LP-Studio — Larkspur Prototype Studio</title>
<link href="https://fonts.googleapis.com/css2?family=Marcellus&family=Open+Sans:wght@400;600;700&display=swap" rel="stylesheet">
<style>
:root{
  --blue:#1c6aa3;
  --blue-dark:#0f4f82;
  --blue-light:#3b8ed0;
  --ink:#1a1a1a;
  --grey-text:#8a8a8a;
  --body-text:#222;
  --band:#e2e2e2;
  --panel:#e4e4dc;
  --dark-btn:#3c3c3c;
  --red:#9e1a2a;
  --serif:'Marcellus', Georgia, serif;
  --sans:'Open Sans', Arial, sans-serif;
}
*{box-sizing:border-box;margin:0;padding:0}
html,body{width:1200px;height:1042px;overflow:hidden;background:#fff;font-family:var(--sans)}
.page{position:relative;width:1200px;height:1042px;overflow:hidden;background:#fff}
.abs{position:absolute}

/* header */
.site-header{left:0;top:0;width:1200px;height:104px;background:linear-gradient(#fdfdfd,#e6e6e6);border-bottom:1px solid #c9c9c9}
.brand{left:128px;top:22px;display:flex;align-items:center;gap:6px}
.brand-mark{width:14px;height:14px;background:var(--blue)}
.brand-name{font-family:var(--serif);font-size:28px;color:var(--blue);line-height:1}
.main-nav a{position:absolute;top:36px;font-family:var(--serif);font-size:17px;color:var(--blue);text-decoration:none;letter-spacing:.3px}
.main-nav a.active{left:216px;top:34px;width:88px;height:28px;background:linear-gradient(#3d95d6,#13609b);color:#fff;text-align:center;line-height:28px;border-radius:2px;box-shadow:0 3px 4px rgba(0,0,0,.2)}
.btn-dark{position:absolute;height:28px;background:linear-gradient(#6a6a6a,#2c2c2c);color:#fff;font-family:var(--serif);font-size:15px;text-align:center;line-height:28px;border-radius:2px;box-shadow:0 3px 4px rgba(0,0,0,.25)}
.cart-widget{left:921px;top:35px;width:126px;height:26px;border:1px solid #d0d0d0;background:#f4f4f4;border-radius:2px}
.cart-widget .label{position:absolute;left:6px;top:5px;width:50px;height:15px;background:linear-gradient(#777,#3a3a3a);color:#fff;font-size:9px;font-weight:700;text-align:center;line-height:15px}
.cart-widget .count{position:absolute;left:85px;top:5px;width:20px;height:15px;background:var(--blue);color:#fff;font-size:9px;font-weight:700;text-align:center;line-height:15px}
.cart-widget .drop{position:absolute;right:2px;top:3px;width:12px;height:18px;background:#bdbdbd;border-radius:2px}

/* hero */
.hero{left:126px;top:104px;width:948px;height:384px;background:linear-gradient(#dcdcdc,#fafafa 60%,#fff);box-shadow:0 0 14px rgba(0,0,0,.18)}
.hero-bg{left:0;top:0;width:948px;height:384px;background:radial-gradient(circle at 60px 60px,rgba(150,150,150,.35),transparent 140px),linear-gradient(90deg,transparent 55%,rgba(180,180,180,.25))}
.hero-title{left:30px;top:34px;font-family:var(--serif);font-size:41px;color:var(--ink)}
.hero-copy{left:30px;top:86px;font-size:14.5px;line-height:24px;color:var(--body-text);white-space:nowrap}
.learn-more{left:484px;top:257px;width:84px;height:24px;background:linear-gradient(#6a6a6a,#2a2a2a);color:#fff;font-family:var(--serif);font-size:13px;line-height:24px;padding-left:6px;clip-path:polygon(0 0,88% 0,100% 50%,88% 100%,0 100%)}
.team-title{left:760px;top:4px;font-family:var(--serif);font-size:25px;color:var(--blue)}
.bios{left:759px;top:43px;width:104px;height:36px;background:linear-gradient(#4aa0dd,#115c98);border:2px solid #fff;box-shadow:0 0 4px rgba(0,0,0,.3);color:#fff;font-family:var(--serif);font-size:19px;text-align:center;line-height:32px}
.hero-product{left:598px;top:96px;width:296px;height:236px;border-radius:10px;background:radial-gradient(ellipse at 78% 30%,rgba(236,140,40,.9),rgba(240,170,100,.5) 35%,transparent 60%),radial-gradient(ellipse at 30% 70%,rgba(150,160,185,.55),transparent 60%),linear-gradient(#eceef1,#f7f7f7)}
.slider-dots{left:410px;top:343px;display:flex;gap:4px}
.slider-dots span{width:22px;height:5px;background:#b9b9b9}
.slider-dots span.on{height:9px;margin-top:-4px;background:#14305a}

/* intro */
.intro-mark{left:146px;top:523px;width:46px;height:52px;background:var(--blue)}
.intro-title{left:208px;top:521px;font-family:var(--serif);font-size:21px;line-height:30px;color:var(--blue)}
.intro-rule{left:145px;top:588px;width:431px;border-top:2px dotted #c9c9c9}
.intro-copy{left:145px;top:597px;font-size:12px;font-weight:600;line-height:20px;color:var(--grey-text);white-space:nowrap}
.read-more{left:502px;top:731px;font-size:12.5px;font-weight:700;color:var(--blue)}

/* tabs */
.tab-box{left:611px;top:524px;width:446px;height:220px;border:2px solid #d3d3d3;border-radius:5px;background:#fff;box-shadow:0 2px 4px rgba(0,0,0,.15)}
.tab{position:absolute;top:4px;font-family:var(--serif);font-size:19px;color:#3a3a3a;line-height:43px}
.tab.active{left:4px;width:97px;height:43px;background:linear-gradient(#3b92d2,#125f9b);color:#fff;text-align:center}
.tab-panel{left:4px;top:48px;width:434px;height:164px;background:var(--panel);border-radius:6px 6px 0 0}
.thumb{position:absolute;top:26px;width:112px;height:112px;background:#fff;border:1px solid #cfcfcf;padding:6px}
.thumb div{width:100%;height:100%;background:radial-gradient(ellipse at 50% 55%,#c7cbd1,#eef0f2 70%)}

/* social band */
.band{left:0;top:790px;width:1200px;height:192px;background:linear-gradient(#d9d9d9,#f2f2f2);border-top:1px solid #cfcfcf;border-bottom:1px solid #c3c3c3}
.band-mid{left:390px;top:790px;width:363px;height:192px;background:radial-gradient(ellipse at 50% 45%,#fff,#e0e0e0 80%)}
.band-title{font-family:var(--serif);font-size:22px;color:var(--blue)}
.band-rule{border-top:1px solid #d0d0d0}
.social-dot{position:absolute;top:862px;width:26px;height:26px;border-radius:50%;background:#4a4a4a}
.social-dot.alt{background:#1eaee3}
.band-copy{left:144px;top:919px;font-size:12.5px;font-weight:600;line-height:20px;color:var(--grey-text)}
.envelopes{left:560px;top:806px;width:170px;height:110px;border-radius:8px;background:radial-gradient(ellipse at 55% 50%,#fbfbfb,#d4d4d4 75%,transparent 76%)}
.subscribe{left:423px;top:870px;width:300px;height:86px;border-radius:8px;background:linear-gradient(#9a9a9a,#5a5a5a);box-shadow:0 3px 5px rgba(0,0,0,.3)}
.subscribe-label{left:12px;top:12px;color:#fff;font-size:15.5px;font-weight:600;letter-spacing:-.3px}
.email{left:16px;top:45px;width:164px;height:32px;background:#ececec;border:2px solid #cfcfcf;font-size:15px;color:#444;line-height:28px;padding-left:6px}
.submit{left:199px;top:43px;width:76px;height:36px;border-radius:4px;background:linear-gradient(#c23044,#7e0f1d);border:2px solid #5d0a14;color:#fff;font-size:17px;font-weight:600;text-align:center;line-height:32px}
.square-icon{left:773px;top:856px;width:30px;height:30px;background:#3b5b98;border-radius:3px}
.like{left:812px;top:858px;width:47px;height:22px;border:1px solid #9aa7c2;background:#eef1f8;border-radius:2px;font-size:11px;color:#3b5998;text-align:center;line-height:20px}
.like-copy{left:867px;top:855px;font-size:10.5px;line-height:14px;color:#444}
.follow-pill{top:909px;height:22px;background:linear-gradient(#fafafa,#d9d9d9);border:1px solid #b8b8b8;font-size:12px;color:#444;line-height:20px;padding-left:10px}
.bird{left:776px;top:930px;width:36px;height:42px;border-radius:50% 50% 45% 45%;background:linear-gradient(#7fcdf0,#2a8fc6)}

/* footer */
.footer-nav{left:144px;top:1004px;display:flex;font-size:12px;color:#333}
.footer-nav span{padding:0 9px}
.footer-nav span:first-child{padding-left:0}
.footer-nav i{color:#bbb;font-style:normal}
.footer-mark{left:779px;top:992px;width:38px;height:42px;background:#4a4a4a}
.copyright{left:833px;top:1004px;font-size:11px;color:#333}
</style>
</head>
<body>
<div class="page">

  <header class="site-header abs">
    <div class="brand abs"><span class="brand-name">LP</span><span class="brand-mark"></span></div>
    <nav class="main-nav">
      <a class="active" href="#">WHY LP</a>
      <a href="#" style="left:342px">DREAMER</a>
      <a href="#" style="left:472px">MAKER</a>
      <a href="#" style="left:584px">PRODUCER</a>
    </nav>
    <div class="btn-dark" style="left:751px;top:34px;width:62px">Login</div>
    <div class="btn-dark" style="left:828px;top:34px;width:78px">Register</div>
    <div class="cart-widget abs">
      <span class="label">SHOP</span>
      <svg style="position:absolute;left:62px;top:4px" width="14" height="16" viewBox="0 0 14 16"><rect x="1" y="5" width="12" height="10" fill="#1c6aa3"/><path d="M4 6V3a3 3 0 0 1 6 0v3" fill="none" stroke="#1c6aa3" stroke-width="1.5"/></svg>
      <span class="count">00</span>
      <span class="drop"></span>
    </div>
  </header>

  <section class="hero abs">
    <div class="hero-bg abs" role="img" aria-label="Faint engineering drawing of gears and a city skyline behind the text"></div>
    <h1 class="hero-title abs">TITLE TEXT</h1>
    <p class="hero-copy abs">Lorem ipsum dolor sit amet, consectetur adipiscing elit. Pellentesque sed lacus<br>neque. Sed urna velit, ullamcorper sit amet facilisis non, tempor id tellus. Donec<br>ullamcorper velit non leo consectetur sit amet ultrices nisl dictum. Suspendisse<br>potenti. Nunc euismod, mauris quis tempus feugiat, sem sapien tempor urna, quis<br>accumsan mi ante at justo. Proin dictum urna at est rutrum vitae lacinia nisl<br>euismod. Proin semper ante nec erat pharetra convallis. Integer rhoncus elit in<br>enim rhoncus eget molestie est bibendum</p>
    <div class="learn-more abs">learn More</div>
    <div class="team-title abs">TEAM LP</div>
    <div class="bios abs">BIOS</div>
    <div class="hero-product abs" role="img" aria-label="Photo of a laptop showing a CAD model beside a desktop 3D printer with an orange cover"></div>
    <div class="slider-dots abs"><span class="on"></span><span></span><span></span><span></span><span></span></div>
  </section>

  <section class="intro">
    <div class="intro-mark abs"></div>
    <h2 class="intro-title abs">Larkspur Prototype Studio<br>What you want ...NOW!</h2>
    <div class="intro-rule abs"></div>
    <p class="intro-copy abs">Lorem ipsum dolor sit amet, consectetur adipiscing elit. Pellentesque<br>sed lacus neque. Sed urna velit, ullamcorper sit amet<br>facilisis non, tempor id tellus. Donec ullamcorper velit non leo<br>consectetur sit amet ultrices nisl dictum. Suspendisse potenti. Nunc<br>euismod, mauris quis tempus feugiat, sem sapien tempor urna, quis<br>accumsan mi ante at justo. Proin dictum urna at est rutrum vitae<br>lacinia nisl euismod.</p>
    <div class="read-more abs">Read Mor &raquo;</div>
  </section>

  <section class="tab-box abs">
    <div class="tab active">STORE</div>
    <div class="tab" style="left:120px">PRINTERS</div>
    <div class="tab" style="left:250px">BLOG</div>
    <div class="tab-panel abs">
      <svg style="position:absolute;left:8px;top:56px" width="14" height="56" viewBox="0 0 14 56"><path d="M12 2 2 28l10 26" fill="none" stroke="#999" stroke-width="4"/></svg>
      <div class="thumb" style="left:32px"><div role="img" aria-label="Photo of an industrial 3D printer"></div></div>
      <div class="thumb" style="left:159px"><div role="img" aria-label="Photo of a desktop 3D printer"></div></div>
      <div class="thumb" style="left:286px"><div role="img" aria-label="Photo of a production 3D printer"></div></div>
      <svg style="position:absolute;left:412px;top:56px" width="14" height="56" viewBox="0 0 14 56"><path d="M2 2l10 26L2 54" fill="none" stroke="#3a9a9a" stroke-width="4"/></svg>
    </div>
  </section>

  <section>
    <div class="band abs"></div>
    <div class="band-mid abs"></div>

    <h3 class="band-title abs" style="left:145px;top:803px">FOLLOW US ON:</h3>
    <div class="band-rule abs" style="left:120px;top:836px;width:262px"></div>
    <span class="social-dot alt" style="left:146px" aria-label="Social network"></span>
    <span class="social-dot" style="left:189px" aria-label="Video channel"></span>
    <span class="social-dot" style="left:232px" aria-label="Social network"></span>
    <span class="social-dot" style="left:275px" aria-label="Social network"></span>
    <span class="social-dot" style="left:318px" aria-label="Email"></span>
    <p class="band-copy abs">Lorem ipsum dolor sit amet, cose<br>&nbsp;adipiscing elit.</p>

    <div class="envelopes abs" role="img" aria-label="Illustration of flying envelopes"></div>
    <div class="subscribe abs">
      <div class="subscribe-label abs">Subscribe to startup news</div>
      <div class="email abs">email@domain.com</div>
      <div class="submit abs">Submit</div>
    </div>

    <h3 class="band-title abs" style="left:803px;top:803px">CONNECT WITH US</h3>
    <div class="band-rule abs" style="left:765px;top:836px;width:290px"></div>
    <div class="square-icon abs"></div>
    <div class="like abs">Like</div>
    <p class="like-copy abs">4 PEOPLE LIKE THIS. BE THE FIRST<br>OF YOUR FRIENDS.</p>
    <div class="follow-pill abs" style="left:807px;width:130px">Follow@lp</div>
    <div class="follow-pill abs" style="left:940px;width:110px;padding-left:15px">337 followers</div>
    <div class="bird abs" role="img" aria-label="Small bird mascot"></div>
  </section>

  <footer>
    <nav class="footer-nav abs">
      <span>Home</span><i>/</i><span>Franchise</span><i>/</i><span>Distributors</span><i>/</i><span>Cart</span><i>/</i><span>Contact</span><i>/</i><span>Blog</span><i>/</i><span>Terms</span><i>/</i><span>Privacy</span>
    </nav>
    <div class="footer-mark abs"></div>
    <p class="copyright abs">Copyright ©2012-2013 All Rights Reserved</p>
  </footer>

</div>
</body>
</html>
```